Kneadwell Haven Business Card Design

I want to create a very elegant and sophisticated two sided business card for my massage practice (www.kneadwellhaven-example.com). I have attached the logo and a PDF with some ideas down for the back of the card but I am open to suggestions. I will want to tie in a post card and flyer to the card later.
Similar colors to website would be great.
Target Market(s)
High end clientele, people looking for a sophisticated spa experience.
Industry/Entity Type
Massage
Contact Information for Business Card
Kneadwell Haven
7218 Larchmont Blvd S, Suite 305
Brookvale, WA 98765
(555) 340-7816
www.kneadwellhaven-example.com

```html
<!DOCTYPE html>
<html lang="en">
<head>
<meta charset="utf-8">
<title>Kneadwell Haven Business Card</title>
<link rel="stylesheet" href="https://fonts.googleapis.com/css2?family=EB+Garamond:ital,wght@0,500;0,700;1,400;1,500&family=Roboto:wght@400&display=swap">
<style>
  :root {
    --navy: #1b3240;
    --paper: #efefef;
    --white: #ffffff;
    --muted: #8c8c8c;
    --ink: #3a3a3a;
    --backdrop: #d9d6d1;
  }
  html, body {
    margin: 0;
    padding: 0;
    overflow: hidden;
  }
  .canvas {
    position: relative;
    width: 1200px;
    height: 538px;
    background: var(--backdrop);
    overflow: hidden;
  }
  .card {
    position: absolute;
    top: 138px;
    height: 262px;
    overflow: hidden;
  }
  .card--front {
    left: 140px;
    width: 456px;
    background: var(--paper);
  }
  .card--back {
    left: 604px;
    width: 458px;
    background: var(--navy);
  }
  .brand-name {
    position: absolute;
    font-family: "EB Garamond", Georgia, serif;
    font-weight: 500;
    font-size: 17px;
    letter-spacing: 0.5px;
    text-transform: uppercase;
    white-space: nowrap;
  }
  .card--front .brand-name {
    left: 26px;
    top: 64px;
    color: var(--navy);
  }
  .card--back .brand-name {
    right: 52px;
    top: 62px;
    color: var(--white);
  }
  .holder-name {
    position: absolute;
    left: 26px;
    top: 143px;
    margin: 0;
    font-family: "EB Garamond", Georgia, serif;
    font-weight: 700;
    font-size: 20px;
    letter-spacing: 0.3px;
    color: var(--navy);
  }
  .holder-role {
    position: absolute;
    left: 26px;
    top: 167px;
    font-family: "EB Garamond", Georgia, serif;
    font-weight: 500;
    font-size: 12.5px;
    color: var(--muted);
  }
  .contact {
    position: absolute;
    left: 26px;
    top: 188px;
    margin: 0;
    padding: 0;
    list-style: none;
    font-family: "Roboto", Arial, sans-serif;
    font-size: 11.5px;
    color: var(--ink);
  }
  .contact li {
    display: flex;
    align-items: center;
    height: 15.5px;
  }
  .contact svg {
    width: 10px;
    height: 10px;
    margin-right: 6px;
    fill: var(--ink);
  }
  .contact .address {
    margin-top: 5px;
  }
  .ornament-area {
    position: absolute;
    top: 0;
    height: 262px;
  }
  .card--front .ornament-area {
    right: 0;
    width: 122px;
    background: linear-gradient(90deg, #c3cbd0 0%, #6f8291 55%, #33495a 100%);
  }
  .card--back .ornament-area {
    left: 0;
    width: 122px;
    background: linear-gradient(90deg, #d3d9dd 0%, #7d8f9b 45%, #2b4252 100%);
  }
  .pitch {
    position: absolute;
    right: 34px;
    top: 140px;
    margin: 0;
    text-align: right;
    font-family: "EB Garamond", Georgia, serif;
    font-style: italic;
    font-weight: 500;
    font-size: 16.5px;
    line-height: 22px;
    color: var(--white);
  }
  .service {
    position: absolute;
    right: 34px;
    top: 216px;
    margin: 0;
    font-family: "EB Garamond", Georgia, serif;
    font-style: italic;
    font-weight: 500;
    font-size: 16.5px;
    color: var(--white);
    white-space: nowrap;
  }
</style>
</head>
<body>
<main class="canvas">
  <section class="card card--front" aria-label="Card front">
    <div class="brand-name">Kneadwell Haven</div>
    <h1 class="holder-name">ELLIOT MARSH</h1>
    <div class="holder-role">CEO/FOUNDER</div>
    <ul class="contact">
      <li>
        <svg viewBox="0 0 24 24" aria-hidden="true"><path d="M6.6 10.8a15.1 15.1 0 0 0 6.6 6.6l2.2-2.2a1 1 0 0 1 1-.25 11.4 11.4 0 0 0 3.6.57 1 1 0 0 1 1 1V20a1 1 0 0 1-1 1A17 17 0 0 1 3 4a1 1 0 0 1 1-1h3.5a1 1 0 0 1 1 1c0 1.25.2 2.45.57 3.57a1 1 0 0 1-.25 1z"/></svg>
        (555) 340-7816
      </li>
      <li>
        <svg viewBox="0 0 24 24" aria-hidden="true"><path d="M12 2a10 10 0 1 0 0 20 10 10 0 0 0 0-20zm-1 17.9A8 8 0 0 1 4.1 10.2L9 15v1a2 2 0 0 0 2 2zm6.9-2.5A2 2 0 0 0 16 16h-1v-3a1 1 0 0 0-1-1H8v-2h2a1 1 0 0 0 1-1V7h2a2 2 0 0 0 2-2v-.4a8 8 0 0 1 2.9 12.8z"/></svg>
        www.kneadwellhaven-example.com
      </li>
      <li class="address">7218 Larchmont Blvd S, Suite 305, Brookvale, WA 98765</li>
    </ul>
    <div class="ornament-area" role="img" aria-label="Large floral mandala decoration in navy on white, cut by the card edge"></div>
  </section>

  <section class="card card--back" aria-label="Card back">
    <div class="ornament-area" role="img" aria-label="Large floral mandala decoration in white on navy, cut by the card edge"></div>
    <div class="brand-name">Kneadwell Haven</div>
    <p class="pitch">Unwind and Discover the Most<br>Restful and Wonderfully Deep<br>Bodywork of Your Year.....</p>
    <p class="service">Slow Tide Full Restoration Bodywork</p>
  </section>
</main>
</body>
</html>
```